Software company specialized in data analytics and professional services

We need a landing page design for our business. It should include our logo design. It should have multiple sections :
- stylish head
- what we do (data analytics software, professional services)
- contact form

Target Market(s)

Companies, B2B

Industry/Entity Type

Data

Number of Pages Required

1 page

Font styles to use
Sans Serif

Requirements
Must have
• Dark theme
Should not have
• Gradients on buttons

```html
<!DOCTYPE html>
<html lang="en">
<head>
<meta charset="utf-8">
<title>LUMENGRID — Data Excellence</title>
<link href="https://fonts.googleapis.com/css2?family=Montserrat:wght@400;500;600;700;800&family=Poppins:wght@400;500;600&display=swap" rel="stylesheet">
<style>
:root{
  --bg:#0b0c1a;
  --text:#ffffff;
  --muted:#c9cbd6;
  --magenta:#c21cc4;
  --button:#7a22b8;
  --purple:#6a3ed8;
  --blue:#3e6fd6;
  --teal:#4fe3c1;
  --pink:#e04a8a;
  --coral:#f07a6a;
  --violet:#7a68f5;
  --field:#111324;
}
*{margin:0;padding:0;box-sizing:border-box}
html,body{width:1200px;height:2708px;overflow:hidden}
body{background:var(--bg);color:var(--text);font-family:"Montserrat",sans-serif;position:relative}
.abs{position:absolute}

/* hero */
.hero-visual{left:0;top:0;width:1200px;height:700px;
  background:radial-gradient(ellipse 420px 380px at 640px 220px,#3a4a6a 0%,#1d2640 45%,transparent 80%),
  radial-gradient(ellipse 300px 260px at 280px 200px,#2a2f3e 0%,transparent 75%),
  linear-gradient(180deg,#11131f 0%,#0b0c1a 100%)}
.logo{left:135px;top:34px;font-weight:700;font-size:32px;letter-spacing:.5px;color:var(--magenta)}
.btn-outline{left:947px;top:30px;width:134px;height:44px;border:1.5px solid var(--magenta);border-radius:22px;
  display:flex;align-items:center;justify-content:center;font-family:"Poppins",sans-serif;font-weight:600;font-size:14px;letter-spacing:.4px}
.hero-kicker{left:0;width:1200px;top:384px;text-align:center;font-weight:500;font-size:17px;letter-spacing:3.2px}
.hero-title{left:0;width:1200px;top:425px;text-align:center;font-weight:800;font-size:68px;letter-spacing:3px;
  background:linear-gradient(90deg,var(--purple) 0%,var(--blue) 45%,var(--teal) 100%);-webkit-background-clip:text;background-clip:text;color:transparent}
.btn-solid{display:flex;align-items:center;justify-content:center;border-radius:24px;font-weight:600;font-size:14px;letter-spacing:1.2px;
  background:var(--button)}
.btn-start{left:523px;top:548px;width:154px;height:44px}

/* about */
.about-band{left:0;top:724px;width:1200px;height:422px;background:linear-gradient(90deg,#1a1020 0%,#0f0d1d 60%,#0c0c1a 100%)}
.about-visual{left:0;top:724px;width:540px;height:422px;
  background:radial-gradient(ellipse 220px 150px at 300px 140px,#7a2a6a 0%,#3a1a3a 50%,transparent 90%),
  radial-gradient(ellipse 240px 120px at 160px 360px,#5a3038 0%,transparent 80%),#150f1e}
.h2{font-weight:800;font-size:32px;letter-spacing:2px}
.about-title{left:618px;top:740px}
.body-text{font-size:13.5px;line-height:21.6px;color:var(--muted)}
.body-text b{color:#fff;font-weight:600}
.about-p1{left:618px;top:815px;width:395px}
.about-p2{left:618px;top:945px;width:405px}
.values{left:618px;top:1052px;display:flex;gap:18px;font-family:"Poppins",sans-serif;font-weight:600;font-size:14px}
.values span{display:flex;align-items:center;gap:6px}

/* services */
.services-title{left:0;width:1200px;top:1234px;text-align:center}
.services-intro{left:320px;width:560px;top:1293px;text-align:center}
.bg-glow{left:0;top:1500px;width:1200px;height:700px;
  background:radial-gradient(ellipse 360px 300px at 200px 260px,rgba(40,90,80,.28) 0%,transparent 75%),
  radial-gradient(ellipse 260px 200px at 1100px 900px,rgba(120,30,120,.25) 0%,transparent 75%)}
.card{top:1376px;width:268px;height:306px;border:1.5px solid #2c2e44;border-radius:12px;padding:36px 22px 36px 26px}
.card svg{display:block;height:44px}
.card-1{left:171px;background:linear-gradient(160deg,#123a38 0%,#0e1222 55%)}
.card-2{left:465px;background:linear-gradient(160deg,#3a1a34 0%,#0e1222 55%)}
.card-3{left:759px;background:linear-gradient(160deg,#242a6a 0%,#0e1222 55%)}
.card h3{margin-top:18px;font-weight:600;font-size:15px;line-height:24px;letter-spacing:.3px}
.card p{margin-top:14px;font-size:13.5px;line-height:21.6px;color:var(--muted)}

/* contact */
.contact-title{left:0;width:1200px;top:1838px;text-align:center}
.field{border:1.5px solid #6a6c80;background:var(--field);border-radius:3px;font-size:14px;padding:0 20px;display:flex;align-items:center}
.f-name{left:285px;top:1913px;width:306px;height:53px}
.f-company{left:608px;top:1913px;width:306px;height:53px}
.f-email{left:285px;top:1990px;width:306px;height:53px}
.f-phone{left:608px;top:1990px;width:306px;height:53px}
.f-message{left:285px;top:2067px;width:629px;height:135px;align-items:flex-start;padding-top:16px;background:#15171f}
.btn-submit{left:544px;top:2238px;width:111px;height:44px}

/* achievements */
.ach-label{left:0;width:1200px;top:2359px;text-align:center;font-size:17px;letter-spacing:3.4px;color:var(--teal);font-weight:500}
.stat{top:2415px;width:260px;text-align:center}
.stat .num{font-weight:600;font-size:58px;letter-spacing:3px;line-height:66px}
.stat .cap{font-size:14px;line-height:21.6px;color:#e0e1ea;margin-top:4px}
.stat-1{left:161px}.stat-1 .num{color:var(--teal)}
.stat-2{left:460px}.stat-2 .num{background:linear-gradient(90deg,var(--pink),var(--coral));-webkit-background-clip:text;background-clip:text;color:transparent}
.stat-3{left:737px}.stat-3 .num{color:var(--violet)}
.stat-3 .cap{margin-top:14px}
.divider{top:2440px;width:1.5px;height:70px;background:#a0166e}

/* footer */
.footer-rule{left:171px;top:2608px;width:860px;height:1.5px;background:#3a3c4a}
.socials{left:173px;top:2641px;display:flex;gap:18px;align-items:center}
.copyright{right:179px;top:2641px;font-size:15px}
.copyright b{font-weight:700}
</style>
</head>
<body>

<div class="abs hero-visual" role="img" aria-label="Photo of an analyst lit by floating data charts and screens"></div>
<div class="abs logo">LUMENGRID</div>
<div class="abs btn-outline">Contact Us</div>
<div class="abs hero-kicker">PIONEERING PRECISION IN</div>
<h1 class="abs hero-title">DATA EXCELLENCE</h1>
<div class="abs btn-solid btn-start">GET STARTED</div>

<section>
  <div class="abs about-band"></div>
  <div class="abs about-visual" role="img" aria-label="Illustration of a hand holding a tablet projecting glowing analytics charts"></div>
  <h2 class="abs h2 about-title">ABOUT LUMENGRID</h2>
  <p class="abs body-text about-p1">At <b>LUMENGRID</b>, we stand at the forefront of innovation, pioneering precision in data excellence. <b>Our mission is</b> to empower businesses with transformative analytics software and expert services, elevating data strategies to new heights.</p>
  <p class="abs body-text about-p2">With a commitment to unlocking insights and unleashing potential, LUMENGRID is your dedicated partner on the journey to data-driven success.</p>
  <div class="abs values">
    <span style="color:var(--teal)"><svg width="14" height="12" viewBox="0 0 14 12"><path d="M1 6l4 4 8-9" fill="none" stroke="currentColor" stroke-width="2"/></svg>Precision</span>
    <span style="color:var(--coral)"><svg width="14" height="12" viewBox="0 0 14 12"><path d="M1 6l4 4 8-9" fill="none" stroke="currentColor" stroke-width="2"/></svg>Innovation</span>
    <span style="color:var(--violet)"><svg width="14" height="12" viewBox="0 0 14 12"><path d="M1 6l4 4 8-9" fill="none" stroke="currentColor" stroke-width="2"/></svg>Partnership</span>
  </div>
</section>

<div class="abs bg-glow"></div>

<section>
  <h2 class="abs h2 services-title">WHAT WE DO</h2>
  <p class="abs body-text services-intro">At <b>LUMENGRID</b>, we redefine the landscape of data analytics, blending cutting-edge software solutions with unparalleled professional services.</p>

  <article class="abs card card-1">
    <svg width="44" height="44" viewBox="0 0 44 44" fill="none" stroke="#4fe3c1" stroke-width="1.6"><circle cx="24" cy="18" r="13"/><path d="M15 27L4 38l3 3 11-11"/><path d="M19 24v-6M24 24V12M29 24v-9"/></svg>
    <h3>PREDICTIVE<br>ANALYTICS SOLUTIONS</h3>
    <p>Harness the power of advanced algorithms and historical data to forecast trends, identify opportunities, and mitigate risks.</p>
  </article>
  <article class="abs card card-2">
    <svg width="44" height="44" viewBox="0 0 44 44" fill="none" stroke="#f07a6a" stroke-width="1.6"><circle cx="8" cy="8" r="6"/><rect x="26" y="2" width="14" height="12" rx="2"/><path d="M29 6h8M29 10h8"/><circle cx="22" cy="24" r="7"/><path d="M19 31h6v4h-6z"/><rect x="2" y="30" width="10" height="10" rx="1"/><circle cx="36" cy="36" r="5"/></svg>
    <h3>CUSTOM DATA<br>STRATEGY CONSULTING</h3>
    <p>From data governance to implementation roadmaps, we guide you on a transformative journey to data excellence.</p>
  </article>
  <article class="abs card card-3">
    <svg width="44" height="44" viewBox="0 -2 44 44" fill="none" stroke="#7a68f5" stroke-width="1.6"><rect x="1" y="1" width="42" height="36" rx="2"/><path d="M1 8h42M32 4.5h2M36 4.5h2M40 4.5h1"/><circle cx="10" cy="20" r="5"/><path d="M10 15v5h5"/><path d="M20 24l6-7 5 4 8-9"/><path d="M6 30h10M20 30h18M20 33h18"/></svg>
    <h3>REAL-TIME REPORTING<br>AND DASHBOARDS</h3>
    <p>Experience the power of instantaneous insights that translate complex data into actionable information.</p>
  </article>
</section>

<section>
  <h2 class="abs h2 contact-title">CONTACT US</h2>
  <div class="abs field f-name">Name</div>
  <div class="abs field f-company">Company</div>
  <div class="abs field f-email">Email</div>
  <div class="abs field f-phone">Phone</div>
  <div class="abs field f-message">Message</div>
  <div class="abs btn-solid btn-submit">SUBMIT</div>
</section>

<section>
  <div class="abs ach-label">ACHIEVEMENTS</div>
  <div class="abs stat stat-1"><div class="num">5</div><div class="cap">years of industry<br>experience</div></div>
  <div class="abs divider" style="left:440px"></div>
  <div class="abs stat stat-2"><div class="num">500%</div><div class="cap">Increase in<br>Operational Efficiency</div></div>
  <div class="abs divider" style="left:739px"></div>
  <div class="abs stat stat-3"><div class="num">20%</div><div class="cap">Revenue Growth</div></div>
</section>

<footer>
  <div class="abs footer-rule"></div>
  <div class="abs socials" aria-label="Social links">
    <svg width="20" height="20"><circle cx="10" cy="10" r="9" fill="#b8bac6"/></svg>
    <svg width="20" height="20"><rect x="1" y="1" width="18" height="18" rx="2" fill="none" stroke="#b8bac6" stroke-width="1.5"/></svg>
    <svg width="20" height="20"><rect x="1" y="1" width="18" height="18" rx="3" fill="#b8bac6"/></svg>
    <svg width="20" height="20"><rect x="1" y="1" width="18" height="18" rx="5" fill="none" stroke="#b8bac6" stroke-width="1.5"/></svg>
    <svg width="22" height="20"><rect x="1" y="3" width="20" height="14" rx="4" fill="#b8bac6"/></svg>
  </div>
  <div class="abs copyright">© 2023 All Rights Reserved | <b>LUMENGRID</b></div>
</footer>

</body>
</html>
```